Review/Re-Design Supermarket E-Commerce website

We have launched our Supermarket E-commerce Website but feel it is lacking a modern feel.

Please re-design the current Supermarket E-commerce site, creating a more modern look and feel.

I am looking for design changes to things such as:

- Fonts
- Button shape & Size
- Shapes of boxes
- Layout of drop down menus
- A new shopping cart / button
- The Header (and in particular the use and positioning of the logo)
- Supplying a generic background image (currently berries)

Please do not change the structure of the page. For instance, the category selection will always be on the left, the items will always be displayed in rows of 3 and the shopping cart should be on the right.
Updates

Current site can be found at www.brovanmarket.com.au

Project Deadline Extended
Reason: designs coming in are generally too different from current design. we are looking for less that 10% change to the overall look and feel. one aspect that needs a lot of work is the checkout cart on the right hand side. please checkout http://www2.pelkinfreshmart.com.au/?gclid=QXRP4kdmwnLBHTYEzJuaPGEKtB

Target Market(s)

Consumers buying their weekly grocery shopping online

Industry/Entity Type

Shopping

Number of Pages Required

1 page

Requirements
Must have
• Stick to the branding of the Logo. Which is Red, Blue and White.
• Other colours may be used in small percentages.
Should not have
• Do not change the Structure of the site.

```html
<!DOCTYPE html>
<html lang="en">
<head>
<meta charset="utf-8">
<title>Brovan Market – Apples</title>
<link rel="stylesheet" href="https://fonts.googleapis.com/css2?family=Arimo:wght@400;700&family=Open+Sans:wght@400;600&display=swap">
<style>
:root{
  --blue:#1d5fa8;
  --navy:#163f78;
  --red:#e3262d;
  --green:#8cc540;
  --green-light:#9fd160;
  --green-dark:#5d9a2a;
  --yellow:#ffd100;
  --grey-line:#b9b9b9;
  --panel:#f4f4f4;
  --text:#222;
  --muted:#777;
}
*{box-sizing:border-box;margin:0;padding:0}
html,body{width:1038px;height:1200px;overflow:hidden;background:#fff}
body{position:relative;font-family:"Arimo",Arial,sans-serif;color:var(--text)}
.abs{position:absolute}

.brand{left:30px;top:58px;font-family:"Open Sans",Arial,sans-serif;font-weight:400;color:var(--blue);line-height:1}
.brand .line1{font-size:42px;letter-spacing:.5px}
.brand .line2{font-size:30px;margin:8px 0 0 46px}
.brand-dot{left:392px;top:58px;width:80px;height:80px;border-radius:50%;background:var(--red)}

.cart-box{left:614px;top:19px;width:189px;height:104px;border:1px solid var(--grey-line);border-radius:8px;background:var(--panel)}
.cart-box .icon{left:8px;top:16px}
.cart-box .count{left:50px;top:30px;font-size:10px}
.cart-box .subl{left:128px;top:20px;font-size:10px}
.cart-box .subv{left:128px;top:36px;font-size:17px}
.cart-box .checkout{left:63px;top:68px;width:55px;height:27px;background:var(--yellow);color:var(--red);font-size:10px;display:flex;align-items:center;justify-content:center}

.collect-box{left:815px;top:19px;width:189px;height:104px;border:1px solid var(--grey-line);border-radius:8px;background:var(--panel);font-size:13px;line-height:15px}
.collect-box .c1{left:32px;top:18px}
.collect-box .d1{left:32px;top:68px}
.collect-box svg{position:absolute}

.side{left:35px;width:226px;border-radius:5px;overflow:hidden;background:var(--green)}
.side li{list-style:none;height:39.4px;display:flex;align-items:center;padding-left:30px;color:#fff;font-size:14px;border-bottom:2px solid var(--green-dark)}
.side li:last-child{border-bottom:none}
.side li.active{background:var(--green-light)}
.favourites{left:35px;top:144px;width:226px;height:38px;background:var(--yellow);color:var(--red);font-weight:700;font-size:15px;display:flex;align-items:center;padding-left:32px}
.favourites svg{position:absolute;left:8px;top:12px}
.specials{left:35px;top:183px;width:226px;height:38px;background:var(--green-dark);color:#fff;font-weight:700;font-size:15px;display:flex;align-items:center;padding-left:33px}

.phone{left:281px;top:156px;color:var(--blue);font-size:19px;display:flex;align-items:center;gap:3px}
.topnav{left:660px;top:154px;display:flex;font-size:11px;color:#555}
.topnav a{color:inherit;text-decoration:none;padding:0 12px;border-right:1px solid #aaa;line-height:18px}
.topnav a:first-child{color:var(--blue)}
.topnav a:last-child{border:none}

.search-icon{left:279px;top:185px;width:34px;height:29px;border:1px solid #ccc}
.search-icon svg{position:absolute;left:8px;top:5px}
.search-input{left:324px;top:185px;width:372px;height:29px;border:1px solid #ccc}
.search-btn{left:700px;top:186px;width:51px;height:27px;background:var(--green);color:#fff;font-size:10px;display:flex;align-items:center;justify-content:center}
.chart-bar{left:759px;top:188px;width:239px;height:42px;background:var(--yellow);color:#fff;font-size:13px;display:flex;align-items:center;padding-left:14px}
.chart-bar b{color:var(--red);font-weight:400;margin:0 4px}
.chart-bar svg{position:absolute;right:10px;top:16px}

.crumbs{left:286px;top:229px;font-size:10px;color:#444;display:flex;gap:20px}
.crumbs span:last-child{color:var(--green)}

.hero{left:277px;top:250px;width:721px;height:305px;background:linear-gradient(100deg,#6f8a2c 0%,#c0392b 25%,#6a2b3c 50%,#3f6b25 70%,#e9ebe0 85%,#6f9a3a 100%)}

.rule{height:3px;background:var(--green);left:277px;width:723px}

.card{width:213px;height:230px;border:2px solid #ccc;background:#fff}
.card .tag{position:absolute;left:0;top:0;width:100%;height:20px;background:var(--green);color:#fff;font-size:11px;display:flex;align-items:center;justify-content:center;gap:4px}
.card .photo{position:absolute;left:50%;top:30px;width:110px;height:100px;margin-left:-55px;border-radius:50%}
.card .name{position:absolute;left:0;right:0;top:140px;text-align:center;font-size:11px}
.card .price{position:absolute;left:20px;top:168px;font-size:16px}
.card .was{position:absolute;left:20px;top:188px;font-size:13px;color:var(--muted)}
.card .qty{position:absolute;left:108px;top:166px;display:flex;align-items:center;gap:14px;font-size:16px}
.card .add{position:absolute;left:105px;top:191px;width:75px;height:27px;border-radius:3px;background:var(--navy);color:#fff;font-size:12px;display:flex;align-items:center;justify-content:center}
.red-apples{background:radial-gradient(circle at 40% 40%,#e8404a,#a3101c)}
.fuji{background:radial-gradient(circle at 40% 40%,#e27a6e,#8e2428)}
.green-apple{background:radial-gradient(circle at 40% 40%,#8fe04a,#3f9a14)}
.rosy{background:radial-gradient(circle at 40% 40%,#ee3a55,#9c0c24)}
.gala{background:radial-gradient(circle at 40% 40%,#f0b04a,#c83a22)}
.yellow-apples{background:radial-gradient(circle at 40% 40%,#d9ec6a,#8fb82a)}
</style>
</head>
<body>

<div class="abs brand"><div class="line1">BROVAN MARKET</div><div class="line2">SUPERMARKETS</div></div>
<div class="abs brand-dot" aria-hidden="true"></div>

<div class="abs cart-box">
  <svg class="abs icon" width="32" height="28" viewBox="0 0 32 28"><path d="M9 10 Q16 0 23 10" fill="none" stroke="#111" stroke-width="2.5"/><rect x="2" y="10" width="28" height="5" rx="1" fill="#111"/><path d="M4 15 H28 L26 27 H6Z" fill="#111"/><g stroke="#fff" stroke-width="1.6"><line x1="10" y1="17" x2="10" y2="25"/><line x1="14" y1="17" x2="14" y2="25"/><line x1="18" y1="17" x2="18" y2="25"/><line x1="22" y1="17" x2="22" y2="25"/></g></svg>
  <div class="abs count">3 items</div>
  <div class="abs subl">Sub Total</div>
  <div class="abs subv">$1.80</div>
  <div class="abs checkout">Checkout</div>
</div>

<div class="abs collect-box">
  <svg width="16" height="16" style="left:10px;top:18px" viewBox="0 0 16 16"><path d="M5 6 V3 a3 3 0 0 1 6 0 V6" fill="none" stroke="#1d5fa8" stroke-width="1.6"/><rect x="1" y="6" width="14" height="10" fill="#1d5fa8"/></svg>
  <div class="abs c1">Click &amp; Collect<br>4/18-22 Marlow street<br>Dunmore TAS 7299</div>
  <svg width="22" height="14" style="left:8px;top:70px" viewBox="0 0 22 14"><rect x="0" y="1" width="13" height="9" fill="#1d5fa8"/><path d="M13 4 H18 L21 7 V10 H13Z" fill="#1d5fa8"/><circle cx="5" cy="11" r="2.3" fill="#1d5fa8" stroke="#f4f4f4"/><circle cx="17" cy="11" r="2.3" fill="#1d5fa8" stroke="#f4f4f4"/></svg>
  <div class="abs d1">Delivery Info</div>
</div>

<div class="abs favourites"><svg width="16" height="15" viewBox="0 0 16 15"><path d="M8 0 L10 5.5 H16 L11 9 L13 15 L8 11 L3 15 L5 9 L0 5.5 H6Z" fill="#f07a1a"/></svg>Favourties</div>
<div class="abs specials">
  <svg class="abs" style="left:12px;top:11px" width="16" height="16" viewBox="0 0 16 16"><circle cx="8" cy="8" r="8" fill="#1f3d12"/><text x="8" y="12" font-size="11" text-anchor="middle" fill="#fff" font-family="Arimo,sans-serif">$</text></svg>
  Online Specials
  <svg class="abs" style="right:22px;top:14px" width="11" height="11" viewBox="0 0 11 11"><path d="M1 1 L5.5 5 L10 1 M1 6 L5.5 10 L10 6" fill="none" stroke="#fff" stroke-width="1.8"/></svg>
</div>
<ul class="abs side" style="top:222px;border-radius:0 0 5px 5px">
  <li class="active">Fruit</li><li>Vegetables</li><li>Meat</li><li>Serviced Deli</li><li>Bakery</li><li>Chilled Foods</li><li>Frozen Food</li><li>Milk</li>
</ul>
<ul class="abs side" style="top:567px">
  <li>Baking Needs</li><li>Beverages</li><li>Biscuits</li><li>Breakfast</li><li>Canned Food</li><li>Cheese</li><li>Chips</li>
</ul>

<div class="abs phone"><svg width="16" height="16" viewBox="0 0 16 16"><path d="M3 1 L6 1 L7 5 L5 6.5 Q6.5 9.5 9.5 11 L11 9 L15 10 L15 13 Q14 15 11 15 Q2 12 1 4 Q1 1 3 1Z" fill="#1d5fa8"/></svg>1300 555 012</div>
<nav class="abs topnav"><a>Products</a><a>Login</a><a>Register</a><a>Products</a><a>My Chart</a></nav>

<div class="abs search-icon"><svg width="18" height="18" viewBox="0 0 18 18"><circle cx="7" cy="7" r="5.5" fill="none" stroke="#999" stroke-width="1.6"/><line x1="11" y1="11" x2="17" y2="17" stroke="#999" stroke-width="1.8"/></svg></div>
<div class="abs search-input"></div>
<div class="abs search-btn">Search</div>
<div class="abs chart-bar">Chart: <b>0</b> Items<svg width="11" height="11" viewBox="0 0 11 11"><path d="M1 1 L5.5 5 L10 1 M1 6 L5.5 10 L10 6" fill="none" stroke="#fff" stroke-width="1.8"/></svg></div>

<div class="abs crumbs"><span>Home</span><span>Fruits</span><span>Apple</span></div>

<div class="abs hero" role="img" aria-label="Fresh produce: wicker basket with grapes, tomatoes, apples, capsicum, cucumbers, cauliflower and leafy greens"></div>

<div class="abs rule" style="top:589px"></div>
<div class="abs rule" style="top:895px"></div>

<div class="abs card" style="left:286px;top:624px">
  <div class="photo red-apples" role="img" aria-label="Bag of red apples"></div>
  <div class="name">Apples Red 2kg Bag</div>
  <div class="price">$8.39</div><div class="was">$8.39</div>
  <div class="qty"><svg width="13" height="13"><circle cx="6.5" cy="6.5" r="6.5" fill="#555"/><rect x="3" y="5.7" width="7" height="1.6" fill="#fff"/></svg>1<svg width="13" height="13"><circle cx="6.5" cy="6.5" r="6.5" fill="#555"/><rect x="3" y="5.7" width="7" height="1.6" fill="#fff"/><rect x="5.7" y="3" width="1.6" height="7" fill="#fff"/></svg></div>
  <div class="add">Add</div>
</div>
<div class="abs card" style="left:536px;top:624px">
  <div class="tag"><svg width="10" height="10"><circle cx="5" cy="5" r="4" fill="none" stroke="#fff"/><path d="M3 5 L4.5 6.5 L7.5 3" fill="none" stroke="#fff"/></svg>Add</div>
  <div class="photo fuji" role="img" aria-label="Single Fuji apple"></div>
  <div class="name">Fuji Apples Each</div>
  <div class="price">$0.06</div><div class="was">$0.06</div>
  <div class="qty"><svg width="13" height="13"><circle cx="6.5" cy="6.5" r="6.5" fill="#555"/><rect x="3" y="5.7" width="7" height="1.6" fill="#fff"/></svg>1<svg width="13" height="13"><circle cx="6.5" cy="6.5" r="6.5" fill="#555"/><rect x="3" y="5.7" width="7" height="1.6" fill="#fff"/><rect x="5.7" y="3" width="1.6" height="7" fill="#fff"/></svg></div>
  <div class="add">Add</div>
</div>
<div class="abs card" style="left:786px;top:624px">
  <div class="tag"><svg width="10" height="10"><circle cx="5" cy="5" r="4" fill="none" stroke="#fff"/><path d="M3 5 L4.5 6.5 L7.5 3" fill="none" stroke="#fff"/></svg>Add</div>
  <div class="photo green-apple" role="img" aria-label="Single green apple"></div>
  <div class="name">Green Apple Each</div>
  <div class="price">$0.06</div><div class="was">$0.06</div>
  <div class="qty"><svg width="13" height="13"><circle cx="6.5" cy="6.5" r="6.5" fill="#555"/><rect x="3" y="5.7" width="7" height="1.6" fill="#fff"/></svg>1<svg width="13" height="13"><circle cx="6.5" cy="6.5" r="6.5" fill="#555"/><rect x="3" y="5.7" width="7" height="1.6" fill="#fff"/><rect x="5.7" y="3" width="1.6" height="7" fill="#fff"/></svg></div>
  <div class="add">Add</div>
</div>

<div class="abs card" style="left:286px;top:933px">
  <div class="tag"><svg width="10" height="10"><circle cx="5" cy="5" r="4" fill="none" stroke="#fff"/><path d="M3 5 L4.5 6.5 L7.5 3" fill="none" stroke="#fff"/></svg>Add</div>
  <div class="photo rosy" role="img" aria-label="Single red apple"></div>
  <div class="name">Rosy Crest Apple Each</div>
  <div class="price">$0.06</div><div class="was">$0.06</div>
  <div class="qty"><svg width="13" height="13"><circle cx="6.5" cy="6.5" r="6.5" fill="#555"/><rect x="3" y="5.7" width="7" height="1.6" fill="#fff"/></svg>1<svg width="13" height="13"><circle cx="6.5" cy="6.5" r="6.5" fill="#555"/><rect x="3" y="5.7" width="7" height="1.6" fill="#fff"/><rect x="5.7" y="3" width="1.6" height="7" fill="#fff"/></svg></div>
  <div class="add">Add</div>
</div>
<div class="abs card" style="left:536px;top:933px">
  <div class="photo gala" role="img" aria-label="Single red and yellow gala apple"></div>
  <div class="name">Royal Gala Apples Each</div>
  <div class="price">$0.06</div><div class="was">$0.06</div>
  <div class="qty"><svg width="13" height="13"><circle cx="6.5" cy="6.5" r="6.5" fill="#555"/><rect x="3" y="5.7" width="7" height="1.6" fill="#fff"/></svg>1<svg width="13" height="13"><circle cx="6.5" cy="6.5" r="6.5" fill="#555"/><rect x="3" y="5.7" width="7" height="1.6" fill="#fff"/><rect x="5.7" y="3" width="1.6" height="7" fill="#fff"/></svg></div>
  <div class="add">Add</div>
</div>
<div class="abs card" style="left:786px;top:933px">
  <div class="photo yellow-apples" role="img" aria-label="Bag of yellow apples"></div>
  <div class="name">Yellow Apple 1.5kg Bag</div>
  <div class="price">$5.20</div><div class="was">$5.20</div>
  <div class="qty"><svg width="13" height="13"><circle cx="6.5" cy="6.5" r="6.5" fill="#555"/><rect x="3" y="5.7" width="7" height="1.6" fill="#fff"/></svg>1<svg width="13" height="13"><circle cx="6.5" cy="6.5" r="6.5" fill="#555"/><rect x="3" y="5.7" width="7" height="1.6" fill="#fff"/><rect x="5.7" y="3" width="1.6" height="7" fill="#fff"/></svg></div>
  <div class="add">Add</div>
</div>

</body>
</html>
```